Whispers of Forgotten Ages - belief and superstition in the past

We need a design for a poster for an upcoming exhibition. The exhibition is called " Whispers of Forgotten Ages - an archaeological exhibition about belief and superstition". Doors will be a key concept in the exhibition, a gateway you have to pass to get to the next room. There are seven rooms with different archaeological objects and stories covering the prehistoric and historic times in Northern Zealand.
The seven rooms has the following titles:
Iconography
Amulets/miniatures
Gold room with objects made of gold
Graves
Fire
Offerings
Christianity
The objects on display are mainly from excavations.
The poster must be in an editable format, as the title has to be in danish.
Target Market(s)
Visitors at museums
Industry/Entity Type
Museum
Requirements
Must have
- A door on the poster,somehow
Nice to have
- Something signalling superstition and belief

```html
<!DOCTYPE html>
<html lang="en">
<head>
<meta charset="utf-8">
<title>Whispers of Forgotten Ages – Exhibition Poster</title>
<link rel="stylesheet" href="https://fonts.googleapis.com/css2?family=Rubik+Dirt&family=Lato:wght@400;700&display=swap">
<style>
  :root {
    --night: #000000;
    --door-bronze: #4b3e25;
    --door-edge-light: #b5aa8c;
    --door-edge-dark: #6f6650;
    --glass-light: #c4bda3;
    --glass-mid: #9d977f;
    --title-ink: #e6d8d3;
    --body-ink: #d3ccc5;
    --logo-ink: #ffffff;
  }
  html, body {
    margin: 0;
    padding: 0;
    width: 800px;
    height: 1200px;
    overflow: hidden;
    background: var(--night);
  }
  .poster {
    position: relative;
    width: 800px;
    height: 1200px;
    background: var(--night);
    overflow: hidden;
    font-family: "Lato", Arial, sans-serif;
  }
  .door-scene {
    position: absolute;
    inset: 0;
    width: 800px;
    height: 1200px;
  }
  .title {
    position: absolute;
    right: 367px;
    top: 282px;
    margin: 0;
    font-family: "Rubik Dirt", "Arial Black", sans-serif;
    font-weight: 400;
    font-size: 62px;
    line-height: 105px;
    text-align: right;
    text-transform: uppercase;
    color: var(--title-ink);
    letter-spacing: 1px;
    white-space: nowrap;
  }
  .title span { display: block; }
  .subtitle {
    position: absolute;
    right: 389px;
    top: 694px;
    margin: 0;
    font-size: 19px;
    line-height: 24px;
    text-align: right;
    color: var(--body-ink);
  }
  .event-details {
    position: absolute;
    right: 389px;
    top: 902px;
    margin: 0;
    font-size: 20px;
    line-height: 25px;
    text-align: right;
    color: var(--body-ink);
  }
  .event-details .time { margin-left: 20px; }
  .event-blurb {
    position: absolute;
    right: 389px;
    top: 964px;
    width: 256px;
    margin: 0;
    font-size: 7.4px;
    line-height: 9.9px;
    text-align: right;
    color: var(--body-ink);
  }
  .museum-mark {
    position: absolute;
    left: 208px;
    top: 1080px;
    display: flex;
    align-items: center;
    gap: 12px;
    color: var(--logo-ink);
    font-family: "Lato", Arial, sans-serif;
    font-weight: 700;
    font-size: 18px;
    line-height: 20px;
    letter-spacing: 0.5px;
  }
  .museum-mark .mark-square {
    width: 40px;
    height: 40px;
    border: 2px solid var(--logo-ink);
    box-sizing: border-box;
  }
</style>
</head>
<body>
<main class="poster">
  <svg class="door-scene" viewBox="0 0 800 1200" xmlns="http://www.w3.org/2000/svg">
    <defs>
      <linearGradient id="door-panel-fade" x1="0" y1="0" x2="1" y2="0">
        <stop offset="0" stop-color="var(--night)"/>
        <stop offset="0.35" stop-color="var(--night)"/>
        <stop offset="1" stop-color="var(--door-bronze)"/>
      </linearGradient>
      <linearGradient id="door-edge-shade" x1="0" y1="0" x2="0" y2="1">
        <stop offset="0" stop-color="var(--door-edge-light)"/>
        <stop offset="0.6" stop-color="var(--door-edge-dark)"/>
        <stop offset="1" stop-color="#4e4838"/>
      </linearGradient>
      <linearGradient id="glass-tone" x1="0" y1="0" x2="0" y2="1">
        <stop offset="0" stop-color="var(--glass-light)"/>
        <stop offset="1" stop-color="var(--glass-mid)"/>
      </linearGradient>
    </defs>

    <polygon class="door-leaf" points="0,30 257,30 476,134 476,1200 0,1200" fill="url(#door-panel-fade)"/>
    <rect class="door-edge" x="460" y="134" width="16" height="1066" fill="url(#door-edge-shade)"/>

    <rect class="window-photo" role="img"
          aria-label="Photo: frosted glass window in the doorway with a shadowy figure pressing its hands against the pane"
          x="522" y="190" width="278" height="640" fill="url(#glass-tone)"/>
  </svg>

  <h1 class="title">
    <span>Whispers</span>
    <span>of</span>
    <span>Forgotten</span>
    <span>Ages</span>
  </h1>

  <p class="subtitle">an archaeological exhibition<br>about belief and superstition</p>

  <p class="event-details">25 Sept 2020<span class="time">6:00pm</span><br>Halvmark Heritage Museum</p>

  <p class="event-blurb">Step through seven rooms of iconography, amulets, gold, graves, fire, offerings and early Christianity. Objects recovered from excavations across the region reveal how people once sought protection, luck and meaning. Discover charms buried beneath floors, gifts left in bogs and symbols carved to ward off harm. Guided tours run every weekend, and families are welcome. Admission is free on opening night, with talks by our archaeologists and light refreshments in the hall.</p>

  <div class="museum-mark">
    <span class="mark-square"></span>
    <span class="mark-name">HALVMARK<br>MUSEUM</span>
  </div>
</main>
</body>
</html>
```